Selkirk Boat Lines and Freight Business Card

I need business cards for my new water taxi and freight transport business I have started here in Kodiak Alaska. Kodiak is a remote island in the middle of the gulf of Alaska. There are seven native villages around the island and Kodiak is the #2 fishing port in the United States. We also have the largest Seaward Corps Base in the U.S. My company will be providing water taxi and freight transport logistics to the villages and many hunting and fishing lodges as well as remote properties around the island.

I would like a business card that isn't status quo, something that stands out, either in feel or appearance. I do like clean minimal designs but it needs to have the necessary contact info on it.

Target Market(s)

remote lodge / property owners, residents of the many villages around Kodiak and any one wanting to enjoy the great outdoors of Kodiak Alaska

Industry/Entity Type

Business

Contact Information for Business Card

I like clean simple designs that aren't cluttered but still provide the necessary information

Colors
0255a3
3277b5
33a4d5
9bcb3c
add136
fbed22
ffc214
f78f20
f37122

Requirements
Must have
• logo and contact info
• Captain Marcus Hollend
• www.selkirkboatlines.com
• marcus@selkirkboatlines.com

```html
<!DOCTYPE html>
<html lang="en">
<head>
<meta charset="utf-8">
<title>Selkirk Boat Lines and Freight – Business Cards</title>
<link href="https://fonts.googleapis.com/css2?family=Mulish:wght@400;700;800&family=Questrial&display=swap" rel="stylesheet">
<style>
  :root{
    --sheet:#ecedec;
    --navy:#1158a6;
    --ink-blue:#1f4f96;
    --sky:#33a4d5;
    --orange:#f78f20;
    --gold:#ffc214;
    --white:#ffffff;
    --shadow:rgba(0,0,0,.28);
  }
  *{box-sizing:border-box;margin:0;padding:0}
  html,body{width:1200px;height:782px;overflow:hidden}
  body{background:var(--sheet);position:relative;font-family:"Questrial",sans-serif}

  .card{position:absolute;width:506px;height:295px;overflow:hidden;box-shadow:0 4px 10px var(--shadow)}
  .card--front{background:var(--navy);color:var(--white);text-align:center}
  .card--back{background:var(--white);height:296px}
  .front-a{left:69px;top:76px}
  .front-b{left:631px;top:76px}
  .back-a{left:66px;top:414px}
  .back-b{left:631px;top:414px}

  /* brand name block */
  .brand{position:absolute;left:0;right:0;font-family:"Mulish",sans-serif;font-weight:800;line-height:1}
  .brand-mark{display:block;margin:0 auto;border-radius:50%;background:var(--orange)}
  .brand-name{display:block;letter-spacing:1px}
  .brand-sub{display:block;letter-spacing:1px}

  .front-a .brand-mark{width:58px;height:58px;margin-bottom:64px}
  .front-a .brand{top:34px}
  .front-a .brand-name{font-size:50px}
  .front-a .brand-sub{font-size:21px;margin-top:8px}
  .front-a .site{top:246px;font-size:19px}

  .front-b .brand{top:28px}
  .front-b .brand-mark{width:54px;height:54px;margin-bottom:56px}
  .front-b .brand-name{font-size:46px}
  .front-b .brand-sub{font-size:19px;margin-top:6px}
  .front-b .site{top:212px;font-size:18px}

  .site{position:absolute;left:0;right:0;letter-spacing:.3px}

  .social{position:absolute;display:flex;gap:9px}
  .social span{display:block;border-radius:50%}
  .front-b .social{top:242px;left:193px}
  .front-b .social span{width:33px;height:33px;background:var(--white)}
  .back-a .social{top:138px;left:350px}
  .back-a .social span{width:33px;height:33px;background:var(--ink-blue)}

  /* back side */
  .person{position:absolute;left:49px;color:var(--ink-blue)}
  .person-name{font-family:"Mulish",sans-serif;font-weight:800;font-size:17px}
  .person-role{font-size:19px;margin-top:2px}
  .contact{list-style:none;margin-top:13px;font-size:17.5px}
  .contact li{display:flex;align-items:center;gap:7px;height:21.5px}
  .contact svg{width:14px;height:14px;flex:none}
  .back-a .person{top:42px}
  .back-b .person{top:30px}

  .back-brand{position:absolute;text-align:center;color:var(--ink-blue);font-family:"Mulish",sans-serif;font-weight:800;line-height:1}
  .back-brand .brand-mark{width:30px;height:30px;margin-bottom:32px}
  .back-brand .brand-name{font-size:27px}
  .back-brand .brand-sub{font-size:11.5px;margin-top:3px;letter-spacing:.4px}
  .back-a .back-brand{left:330px;width:140px;top:24px}
  .back-b .back-brand{left:330px;width:140px;top:40px}

  .accent-band{position:absolute;left:0;right:0;top:176px;height:12px;
    background:linear-gradient(90deg,transparent 0%,var(--orange) 8%,var(--gold) 40%,var(--orange) 70%,transparent 100%);opacity:.9}
  .scene{position:absolute;left:0;right:0;top:188px;bottom:0;
    background:linear-gradient(180deg,#3d86d6 0%,#8fc2ea 32%,#2a5f93 52%,#1c4f86 72%,#7fb1de 100%)}
</style>
</head>
<body>

  <!-- front, plain -->
  <section class="card card--front front-a">
    <div class="brand">
      <span class="brand-mark"></span>
      <span class="brand-name">SELKIRK</span>
      <span class="brand-sub">Boat Lines &amp; Freight</span>
    </div>
    <p class="site">www.selkirkboatlines.com</p>
  </section>

  <!-- front, with social -->
  <section class="card card--front front-b">
    <div class="brand">
      <span class="brand-mark"></span>
      <span class="brand-name">SELKIRK</span>
      <span class="brand-sub">Boat Lines &amp; Freight</span>
    </div>
    <p class="site">www.selkirkboatlines.com</p>
    <div class="social" aria-label="Social profiles"><span></span><span></span><span></span></div>
  </section>

  <!-- back, with social -->
  <section class="card card--back back-a">
    <div class="person">
      <p class="person-name">Marcus Hollend</p>
      <p class="person-role">Captain</p>
      <ul class="contact">
        <li><svg viewBox="0 0 14 14"><rect x="3.5" y="1" width="7" height="12" rx="1.3" fill="none" stroke="#f78f20" stroke-width="1.3"/><line x1="6" y1="11" x2="8" y2="11" stroke="#f78f20" stroke-width="1.2"/></svg>907-555-0148</li>
        <li><svg viewBox="0 0 14 14"><rect x="1" y="3" width="12" height="8.5" fill="none" stroke="#f78f20" stroke-width="1.3"/><polyline points="1,3 7,8 13,3" fill="none" stroke="#f78f20" stroke-width="1.2"/></svg>marcus@selkirkboatlines.com</li>
        <li><svg viewBox="0 0 14 14"><circle cx="7" cy="7" r="5.8" fill="none" stroke="#f78f20" stroke-width="1.3"/><ellipse cx="7" cy="7" rx="2.5" ry="5.8" fill="none" stroke="#f78f20" stroke-width="1"/><line x1="1.2" y1="7" x2="12.8" y2="7" stroke="#f78f20" stroke-width="1"/></svg>www.selkirkboatlines.com</li>
      </ul>
    </div>
    <div class="back-brand">
      <span class="brand-mark"></span>
      <span class="brand-name">SELKIRK</span>
      <span class="brand-sub">Boat Lines &amp; Freight</span>
    </div>
    <div class="social" aria-label="Social profiles"><span></span><span></span><span></span></div>
    <div class="accent-band" role="img" aria-label="Orange brushstroke accent"></div>
    <div class="scene" role="img" aria-label="Photo of a boat wake on a calm bay with mountains at sunset"></div>
  </section>

  <!-- back, plain -->
  <section class="card card--back back-b">
    <div class="person">
      <p class="person-name">Marcus Hollend</p>
      <p class="person-role">Captain</p>
      <ul class="contact">
        <li><svg viewBox="0 0 14 14"><rect x="3.5" y="1" width="7" height="12" rx="1.3" fill="none" stroke="#f78f20" stroke-width="1.3"/><line x1="6" y1="11" x2="8" y2="11" stroke="#f78f20" stroke-width="1.2"/></svg>907-555-0148</li>
        <li><svg viewBox="0 0 14 14"><rect x="1" y="3" width="12" height="8.5" fill="none" stroke="#f78f20" stroke-width="1.3"/><polyline points="1,3 7,8 13,3" fill="none" stroke="#f78f20" stroke-width="1.2"/></svg>marcus@selkirkboatlines.com</li>
        <li><svg viewBox="0 0 14 14"><circle cx="7" cy="7" r="5.8" fill="none" stroke="#f78f20" stroke-width="1.3"/><ellipse cx="7" cy="7" rx="2.5" ry="5.8" fill="none" stroke="#f78f20" stroke-width="1"/><line x1="1.2" y1="7" x2="12.8" y2="7" stroke="#f78f20" stroke-width="1"/></svg>www.selkirkboatlines.com</li>
      </ul>
    </div>
    <div class="back-brand">
      <span class="brand-mark"></span>
      <span class="brand-name">SELKIRK</span>
      <span class="brand-sub">Boat Lines &amp; Freight</span>
    </div>
    <div class="accent-band" role="img" aria-label="Orange brushstroke accent"></div>
    <div class="scene" role="img" aria-label="Photo of a boat wake on a calm bay with mountains at sunset"></div>
  </section>

</body>
</html>
```